Shop Window Signs and Fence Designs

Hi guys im looking for creativity people in helping me with these designs 50 all up

Designs on various signage displays for shop windows and store fronts.

50 separate designs with on going work available.
Each design to be suppled in PDF

20 - Vertical designs - (posters)
20 - Horizontal designs - (banners) for hanging on fences e.g.
5 - Vertical - sales, garage sale EG
5 - Horizontal - sales, garage sale EG

MIX THINGS UP GUYS these are my samples below

At this stage only looking at straight eges designs.

COLOUR FULL DESIGNS EYE CATCHING
thanks guys lots more work to come for the right designer

Target Market(s)

Customers - Shoppers

Industry/Entity Type

Shop

Font styles to use
Serif
Sans Serif
Decorative
Script

Colors

Designer to choose colors to be used in the design.

Requirements
Must have
• POSTERS - in VERTICAL format
• 1900 x 1320 200gsm
• 2600 x 1600 200gsm
• 1540 x 1060 250gsm
• 2440 x1320 200gsm
• BANNERS - in HORIZONTAL format
• 1000 x 5000
• 1000 x 4000
• 1000 x 3000
• 1000 x 2000
Nice to have
• Be creative
Should not have
• Be creative

```html
<!DOCTYPE html>
<html lang="en">
<head>
<meta charset="utf-8">
<title>End of Season Clearance Banner</title>
<link href="https://fonts.googleapis.com/css2?family=Jost:wght@500;600;700&family=Open+Sans:wght@400;700&display=swap" rel="stylesheet">
<style>
  :root {
    --plum: #5c2161;
    --orchid: #8e3d97;
    --sale-red: #c0202e;
    --sun-yellow: #f9e03b;
    --panel-black: #000000;
    --white: #ffffff;
    --ink: #1a1a1a;
  }
  html, body {
    margin: 0;
    padding: 0;
    width: 1200px;
    height: 240px;
    overflow: hidden;
    background: var(--white);
  }
  .banner {
    display: block;
    width: 1200px;
    height: 240px;
  }
  .bg-plum { fill: var(--plum); }
  .bg-orchid { fill: var(--orchid); }
  .badge-ring { fill: var(--sun-yellow); }
  .badge-fill { fill: var(--sale-red); }
  .contact-panel { fill: var(--panel-black); }
  .web-box { fill: var(--sun-yellow); }

  .badge-text {
    font-family: "Jost", sans-serif;
    font-weight: 600;
    font-size: 46px;
    fill: var(--sun-yellow);
  }
  .discount {
    font-family: "Jost", sans-serif;
    font-weight: 700;
    fill: var(--sun-yellow);
  }
  .discount-range { font-size: 140px; }
  .discount-percent { font-size: 86px; }
  .discount-off { font-size: 60px; }
  .discount-scope { font-size: 60px; font-weight: 600; }

  .logo-name {
    font-family: "Open Sans", sans-serif;
    font-weight: 700;
    font-size: 40px;
    fill: var(--white);
  }
  .company-name {
    font-family: "Open Sans", sans-serif;
    font-weight: 400;
    font-size: 24px;
    fill: var(--white);
  }
  .phone-number {
    font-family: "Open Sans", sans-serif;
    font-weight: 700;
    font-size: 25px;
    fill: var(--white);
  }
  .phone-icon { fill: var(--white); }
  .web-address {
    font-family: "Open Sans", sans-serif;
    font-weight: 400;
    font-size: 17px;
    fill: var(--ink);
  }
</style>
</head>
<body>
<svg class="banner" viewBox="0 0 1500 300" xmlns="http://www.w3.org/2000/svg" role="img" aria-label="End of season clearance, 50 to 70 percent off all ladies apparel">
  <!-- background -->
  <rect class="bg-plum" x="0" y="0" width="1185" height="300"/>
  <path class="bg-orchid" d="M0,0 H1185 V45 H575 C470,45 420,95 360,160 C310,212 250,230 0,230 Z"/>

  <!-- clearance badge -->
  <circle class="badge-ring" cx="200" cy="2" r="192"/>
  <circle class="badge-fill" cx="196" cy="-6" r="188"/>
  <text class="badge-text">
    <tspan x="78" y="56">end of</tspan>
    <tspan x="76" y="97">season</tspan>
    <tspan x="76" y="137">clearance</tspan>
  </text>

  <!-- offer -->
  <text class="discount discount-range" x="572" y="196" textLength="398" lengthAdjust="spacingAndGlyphs">50-70</text>
  <text class="discount discount-percent" x="978" y="139" textLength="106" lengthAdjust="spacingAndGlyphs">%</text>
  <text class="discount discount-off" x="978" y="194" textLength="122" lengthAdjust="spacingAndGlyphs">OFF</text>
  <text class="discount discount-scope" x="580" y="259" textLength="508" lengthAdjust="spacingAndGlyphs">all ladies apparel</text>

  <!-- contact panel -->
  <rect class="contact-panel" x="1185" y="0" width="315" height="300"/>
  <text class="logo-name" x="1347" y="72" text-anchor="middle">Logo</text>
  <text class="company-name" x="1346" y="186" text-anchor="middle">company name</text>
  <path class="phone-icon" d="M1246,206 c2,-2 5,-2 6,0 l4,6 c1,2 0,4 -1,5 l-2,2 c1,3 5,8 8,10 l2,-2 c1,-1 3,-2 5,-1 l6,4 c2,1 2,4 0,6 l-3,3 c-3,3 -9,1 -15,-4 c-6,-5 -11,-12 -12,-17 c-1,-4 0,-7 2,-9 Z"/>
  <text class="phone-number" x="1272" y="226">000 000 0000</text>
  <rect class="web-box" x="1212" y="242" width="268" height="58"/>
  <text class="web-address" x="1346" y="272" text-anchor="middle">www.company name.com</text>
</svg>
</body>
</html>
```